Ad Design for a child care centre

Bright Pebbles Child Care Centre offers a safe, nurturing environment where your child will get the attention and care that he or she needs. Our ratio of children to adults is always within state guidelines - and often even higher - to make certain each child receives top-quality care
We are also state licensed as a Child Care facility and have met or exceeded all health and safety guidelines.
3-5 year Kinder Funded Program
Story Time
Show and Tell
Puzzles and Games
Computer Time
Arts and Crafts
Music
Pre-Reading Activities
And much more
You can rest assured that your child will be cared for with the most kindness, love and respect. We believe all children are precious gifts and we treat them as though they are our own.
Full-time, part-time, Half days, Before, after-school schedules are available.
To learn more, contact us today! 03 9514 -0817 or info@brightpebbles.example.au

```html
<!DOCTYPE html>
<html lang="en">
<head>
<meta charset="utf-8">
<title>Bright Pebbles Child Care Centre – Ad</title>
<link href="https://fonts.googleapis.com/css2?family=Tinos:ital,wght@0,400;0,700;1,400;1,700&display=swap" rel="stylesheet">
<style>
  :root {
    --pink: #f5a9c8;
    --pink-text: #f6aacb;
    --crimson: #a72841;
    --maroon: #6d1127;
    --maroon-deep: #7a1430;
    --ink: #1c1c1c;
    --black: #000000;
    --white: #ffffff;
  }
  * { margin: 0; padding: 0; box-sizing: border-box; }
  html, body { width: 1200px; height: 848px; overflow: hidden; background: var(--pink); }
  .ad {
    position: relative;
    width: 1200px;
    height: 848px;
    overflow: hidden;
    background: var(--pink);
    font-family: "Tinos", "Times New Roman", serif;
    color: var(--ink);
  }
  .ad-shapes { position: absolute; inset: 0; }
  .ad-title {
    position: absolute;
    top: 56px; left: 0; width: 1200px;
    text-align: center;
    font-size: 58px;
    font-weight: 700;
    font-style: italic;
    color: var(--white);
    letter-spacing: 0.5px;
  }
  .intro {
    position: absolute;
    top: 168px; left: 34px; width: 700px;
    font-size: 21.5px;
    line-height: 1.3;
    text-align: justify;
  }
  .intro p + p { margin-top: 28px; }
  .intro em { font-style: italic; }
  .intro .brand { font-style: italic; font-weight: 700; }
  .photo {
    position: absolute;
    left: 28px; top: 492px;
    width: 228px; height: 228px;
    border-radius: 50%;
    background: radial-gradient(circle at 45% 40%, #c9836f 0%, #7f8f6a 55%, #4f6f8a 100%);
    border: 3px solid var(--white);
  }
  .promise {
    position: absolute;
    top: 514px; left: 272px; width: 462px;
    text-align: center;
    font-size: 20.5px;
    line-height: 1.38;
    font-weight: 700;
    font-style: italic;
  }
  .activities {
    position: absolute;
    top: 188px; left: 751px; width: 449px;
    list-style: none;
    text-align: center;
    color: var(--pink-text);
    font-size: 38.5px;
    line-height: 51.5px;
    font-weight: 700;
    font-style: italic;
  }
  .contact {
    position: absolute;
    left: 744px; top: 621px;
    width: 447px; height: 167px;
    background: var(--black);
    color: var(--white);
    text-align: center;
    padding-top: 14px;
  }
  .contact-lead { font-size: 23px; }
  .contact-phone, .contact-email { font-weight: 700; font-style: italic; }
  .contact-phone { font-size: 38px; margin-top: 6px; }
  .contact-email { font-size: 30.5px; margin-top: 6px; }
  .website {
    position: absolute;
    left: 751px; top: 807px; width: 449px;
    text-align: center;
    color: var(--pink-text);
    font-size: 18px;
    letter-spacing: 4.6px;
  }
  .schedules {
    position: absolute;
    top: 757px; left: 0; width: 718px;
    text-align: center;
    color: var(--pink-text);
    font-size: 28.5px;
    line-height: 38px;
    font-weight: 700;
    font-style: italic;
  }
</style>
</head>
<body>
<main class="ad">
  <svg class="ad-shapes" width="1200" height="848" viewBox="0 0 1200 848" aria-hidden="true">
    <path class="band-top" d="M0,0 H1200 V118 C980,112 860,118 751,140 C560,178 300,168 0,150 Z" fill="var(--crimson)"/>
    <rect class="panel-right" x="751" y="118" width="449" height="730" fill="var(--maroon)"/>
    <path class="band-bottom" d="M0,684 C180,722 420,730 751,664 V848 H0 Z" fill="var(--maroon-deep)"/>
  </svg>

  <h1 class="ad-title">Bright Pebbles Child Care Centre</h1>

  <section class="intro">
    <p><span class="brand">Bright Pebbles<br>Child Care Centre</span> offers a <em>safe, nurturing environment</em> where your child will get the attention and care that he or she needs. Our ratio of children to adults is always within state guidelines - and often even higher - to make certain each child receives <em>top-quality care</em></p>
    <p>We are also <em>state licensed</em> as a <em>Child Care facility</em> and have met or exceeded all <em>health</em> and <em>safety guidelines</em>.</p>
  </section>

  <div class="photo" role="img" aria-label="Photo of two smiling young children playing outdoors at a playground"></div>

  <p class="promise">You can rest assured that your child will be cared for with the most kindness, love and respect. We believe all children are precious gifts and we treat them as though they are our own.</p>

  <ul class="activities">
    <li>Story Time</li>
    <li>Show and Tell</li>
    <li>Puzzles and Games</li>
    <li>Computer Time</li>
    <li>Arts and Crafts</li>
    <li>Music</li>
    <li>Pre-Reading Activities</li>
    <li>and Much More</li>
  </ul>

  <section class="contact">
    <p class="contact-lead">To learn more, contact us today!</p>
    <p class="contact-phone">03 9514 -0817</p>
    <p class="contact-email">info@brightpebbles.example.au</p>
  </section>

  <p class="website">www.brightpebbles.example.au</p>

  <p class="schedules">Full-time, part-time, Half days,<br>Before &amp; After-school schedules are available</p>
</main>
</body>
</html>
```